Fundraising Study Day East of England. Lift the January blues!

A flyer to advertise a fundraising event of lectures for dental hygienists and therapists in support of the exemption campaign. Currently dental hygienists and therapists require a prescription to deliver certain treatment or recommend certain toothpastes. If we are successful in the campaign we will be able to treat patients without these restrictions.

Industry/Entity Type

Dental

```html
<!DOCTYPE html>
<html lang="en">
<head>
<meta charset="utf-8">
<title>Fundraising Study Day East of England – Lift the January Blues!</title>
<link rel="stylesheet" href="https://fonts.googleapis.com/css2?family=Bangers&family=Montserrat:wght@400;600;700&family=Source+Sans+3:wght@400;700&display=swap">
<style>
  :root {
    --blue: #3a4fa3;
    --blue-deep: #34479a;
    --orange: #f26f21;
    --teal: #2bb5a7;
    --ink: #231f20;
    --agenda-bg: #d9dded;
    --white: #ffffff;
    --sky-top: #c9d9e6;
    --sky-bottom: #f4f7fa;
  }
  html, body {
    margin: 0;
    padding: 0;
    width: 927px;
    height: 1200px;
    overflow: hidden;
    background: var(--white);
  }
  .flyer {
    position: relative;
    width: 927px;
    height: 1200px;
    overflow: hidden;
    font-family: "Source Sans 3", Arial, sans-serif;
    color: var(--ink);
  }
  .winter-backdrop {
    position: absolute;
    inset: 0 0 568px 0;
    background: linear-gradient(170deg, var(--sky-top) 0%, #e6eef4 45%, var(--sky-bottom) 100%);
  }
  .event-series {
    position: absolute;
    top: 24px;
    left: 0;
    width: 100%;
    margin: 0;
    text-align: center;
    font-family: "Bangers", Impact, sans-serif;
    font-weight: 400;
    font-size: 42px;
    letter-spacing: 2px;
    color: var(--blue);
  }
  .headline {
    position: absolute;
    top: 120px;
    left: 0;
    width: 100%;
    margin: 0;
    text-align: center;
    font-family: "Bangers", Impact, sans-serif;
    font-weight: 400;
    line-height: 0.9;
    transform: rotate(-7deg);
  }
  .headline-lift {
    display: block;
    color: var(--orange);
    font-size: 104px;
    letter-spacing: 2px;
    margin-left: 40px;
  }
  .headline-blues {
    display: block;
    color: var(--blue);
    font-size: 100px;
    letter-spacing: 2px;
    margin-left: 30px;
  }
  .ornament { position: absolute; }
  .marker-triangle { left: 296px; top: 104px; }
  .rocket-left { left: 148px; top: 182px; width: 110px; height: 60px; border-radius: 30px; background: var(--teal); transform: rotate(30deg); }
  .rocket-right { left: 640px; top: 110px; width: 120px; height: 60px; border-radius: 30px; background: var(--teal); transform: rotate(-40deg); }
  .badge-left { left: 118px; top: 286px; width: 102px; height: 102px; border-radius: 50%; background: var(--orange); }
  .badge-right { left: 708px; top: 225px; width: 102px; height: 102px; border-radius: 50%; background: var(--orange); }

  .event-details {
    position: absolute;
    top: 418px;
    left: 0;
    width: 100%;
    text-align: center;
    font-family: "Montserrat", Arial, sans-serif;
  }
  .event-details p { margin: 0; }
  .event-date { font-size: 33px; font-weight: 700; color: var(--ink); line-height: 44px; }
  .event-time { font-size: 33px; font-weight: 700; color: var(--blue); line-height: 44px; }
  .event-venue { font-size: 21px; font-weight: 600; line-height: 28px; margin-top: 8px !important; }
  .event-address { font-size: 21px; font-weight: 400; line-height: 28px; }
  .event-cost { font-size: 31px; font-weight: 700; color: var(--blue); line-height: 42px; margin-top: 4px !important; }

  .intro-band {
    position: absolute;
    top: 632px;
    left: 0;
    width: 100%;
    height: 108px;
    background: var(--blue-deep);
  }
  .intro-band p {
    margin: 12px 0 0 148px;
    width: 640px;
    color: var(--white);
    font-size: 17px;
    line-height: 21px;
  }
  .intro-pointer { position: absolute; left: 440px; top: 739px; }

  .agenda {
    position: absolute;
    top: 740px;
    left: 0;
    width: 100%;
    height: 412px;
    background: var(--agenda-bg);
  }
  .agenda-title {
    position: absolute;
    top: 30px;
    left: 0;
    width: 100%;
    margin: 0;
    text-align: center;
    font-family: "Montserrat", Arial, sans-serif;
    font-weight: 700;
    font-size: 25px;
    letter-spacing: 3px;
    color: var(--ink);
  }
  .agenda-column { position: absolute; font-size: 15.5px; line-height: 19px; }
  .agenda-left { left: 55px; top: 76px; width: 382px; }
  .agenda-right { left: 476px; top: 76px; width: 397px; }
  .agenda-closing { left: 268px; top: 306px; width: 400px; }
  .slot-time { margin: 0; font-weight: 700; }
  .slot-desc { margin: 0 0 8px; text-align: justify; }
  .slot-break { margin: 0 0 8px; font-weight: 700; }

  .link-band {
    position: absolute;
    top: 1152px;
    left: 0;
    width: 100%;
    height: 48px;
    background: var(--blue-deep);
  }
  .link-band p {
    margin: 10px 0 0;
    text-align: center;
    color: var(--white);
    font-weight: 700;
    font-size: 14.5px;
  }
  .link-band .edge-line {
    position: absolute;
    bottom: 5px;
    left: 0;
    width: 100%;
    height: 3px;
    background: rgba(255,255,255,0.35);
  }
</style>
</head>
<body>
<main class="flyer">
  <div class="winter-backdrop" role="img" aria-label="Soft photograph of snow-dusted pine needles in pale winter light"></div>

  <h1 class="event-series">Fundraising Study Day East of England</h1>

  <svg class="ornament marker-triangle" width="36" height="30" viewBox="0 0 36 30" aria-hidden="true">
    <polygon points="18,0 36,30 0,30" fill="var(--blue)"/>
  </svg>
  <div class="ornament rocket-left" role="img" aria-label="Teal rocket illustration"></div>
  <div class="ornament rocket-right" role="img" aria-label="Teal rocket illustration"></div>
  <div class="ornament badge-left" role="img" aria-label="Orange snowflake badge"></div>
  <div class="ornament badge-right" role="img" aria-label="Orange snowflake badge"></div>

  <h2 class="headline">
    <span class="headline-lift">Lift the</span>
    <span class="headline-blues">January Blues!</span>
  </h2>

  <section class="event-details">
    <p class="event-date">FRIDAY |19 JANUARY 2018</p>
    <p class="event-time">09:00 – 16:30 GMT</p>
    <p class="event-venue">HARLOW COURT HOTEL</p>
    <p class="event-address">MERIDIAN WAY, WELBURY, WB4 2QT</p>
    <p class="event-cost">COST - £101.48</p>
  </section>

  <section class="intro-band">
    <p>A fundraising event to support our exemptions project. The day will consist of a series of presentations ranging from the new ECPD to new technologies. The aim, being to enhance our learning and raise funds to support the exemptions campaign. The speaker line includes some of the UK and Irelands most respected dental professionals in our field.</p>
  </section>

  <section class="agenda">
    <h3 class="agenda-title">AGENDA</h3>

    <div class="agenda-column agenda-left">
      <p class="slot-time">9.30 - 10.15</p>
      <p class="slot-desc">Nora Whitfield: Immediate past president of the ADHT will be updating us on all things ECPD</p>
      <p class="slot-time">10.15 - 11.00</p>
      <p class="slot-desc">Tessa Marlow: Will provide an update on teeth whiteing and explain how social media has impacted her business</p>
      <p class="slot-desc">Helena Brooke: Our internationally acclaimed speaker will update our knowledge of periodontal disease and nutrition and new technologies.</p>
      <p class="slot-break">11.00 - 11.30 BREAK</p>
    </div>

    <div class="agenda-column agenda-right">
      <p class="slot-time">11.30 - 13.00</p>
      <p class="slot-desc">Ciara Donnelly &amp; Rachel Ambrose: Will be providing a combined presentation on ‘Scaling your business’ and start to finish Sonoflow techniques. The aim being to build our business with effective communications, systems and protocols. This sessions promises audience participation!</p>
      <p class="slot-break">12 - 1400 LUNCH</p>
      <p class="slot-time">14 - 15.00</p>
      <p class="slot-desc" style="margin-bottom:2px">Priya Desai: Save your back. All things posture.</p>
      <p class="slot-break">15.00 - 15.30 BREAK</p>
    </div>

    <div class="agenda-column agenda-closing">
      <p class="slot-time">15.30 16.30</p>
      <p class="slot-desc">Helena Brooke: Our internationally acclaimed speaker will update our knowledge of periodontal disease and nutrition and new technologies.</p>
    </div>
  </section>

  <svg class="intro-pointer" width="46" height="18" viewBox="0 0 46 18" aria-hidden="true">
    <polygon points="0,0 46,0 23,18" fill="var(--blue-deep)"/>
  </svg>

  <footer class="link-band">
    <p>https://www.eventpass.example/e/fundraising-study-day-east-of-england-lift-the-january-blues-tickets-48210357</p>
    <div class="edge-line"></div>
  </footer>
</main>
</body>
</html>
```